Varnek Group Business Card

Varnek Group — Business Card Design Brief
Overview
Design a double-sided business card for Varnek Group that highlights our two service arms: Varnek Communications (telecommunications) and Varnek Energy (business energy solutions). The card should feel smart and stand out when handed to clients.

Objectives
Showcase our areas of specialty clearly.
Reflect the overall Varnek / Varnek Group brand while acknowledging both arms.
Explore using both logos (Communications + Energy) or one unified logo, depending on the design.

Deliverables
One double-sided business card design (front + back).

Content & Copy
Front (preferred): Logo: Varnek / Varnek Group
Descriptor: Business Communications | Business Energy
Back:My contact details and company details
Core products: Business Mobile • Telephony • Internet • Business Energy Solutions

Brand & Visual Direction
We have a group logo currently tailored more toward telecoms, plus a separate Varnek Energy logo.
Please explore layouts that use both logos or just one, whichever works best.
Color: I wouldn't mind seeing an option using our the Blue/Purple gradient from our website (varnek-example.co.uk), but also open to non-gradient approaches and other colours..

Overall look: Smart, modern, and distinctive.
Format & Print Specs
Double-sided business card format. (Use a standard size

Must-Haves
Front: Varnek wording or Varnek Group wording with atleast 1 logo also on front “Business Communications | Business Energy.”

Back: Contact + company details and core products.
A design that stands out while remaining professional.

Nice-to-Have Options
A gradient version using our site’s Blue/Purple gradient.
A non-gradient version.
A dual-logo treatment versus a single-logo treatment.

Thanks
Dominic

```html
<!DOCTYPE html>
<html lang="en">
<head>
<meta charset="utf-8">
<title>Varnek Group Business Card</title>
<link rel="stylesheet" href="https://fonts.googleapis.com/css2?family=Montserrat:wght@400;500;600;700&family=Poppins:wght@600;700&display=swap">
<style>
  :root {
    --bg: #d3d4d6;
    --card: #fdfbf4;
    --panel: #ffffff;
    --ink: #26205e;
    --text: #222222;
    --accent: #983c8e;
    --comms: #2f5fb8;
    --energy: #2f9e3a;
  }
  * { margin: 0; padding: 0; box-sizing: border-box; }
  html, body { width: 900px; height: 1200px; overflow: hidden; }
  body { background: var(--bg); position: relative; font-family: "Montserrat", sans-serif; color: var(--text); }

  .card { position: absolute; left: 149px; width: 602px; height: 388px; background: var(--card); }
  .card--front { top: 168px; }
  .card--back { top: 644px; }

  .brand { position: absolute; }
  .brand--comms { left: 46px; top: 91px; }
  .brand--energy { left: 323px; top: 91px; }
  .brand__mark { display: block; width: 118px; height: 118px; margin-left: 0; }
  .brand--energy .brand__mark { margin-left: 0; }
  .brand__name {
    font-family: "Poppins", sans-serif; font-weight: 700; font-size: 64px;
    line-height: 1; color: var(--ink); letter-spacing: -0.5px; margin-top: 10px;
  }
  .brand__descriptor {
    font-family: "Poppins", sans-serif; font-weight: 600; font-size: 14.5px;
    color: var(--text); letter-spacing: 0.9px; margin-top: 14px; margin-left: 3px;
  }

  .back-panel { position: absolute; left: 22px; top: 144px; right: 0; bottom: 0; background: var(--panel); }

  .person { position: absolute; right: 331px; top: 170px; text-align: right; }
  .person__name { font-weight: 700; font-size: 25px; color: var(--ink); line-height: 1.1; }
  .person__role { font-size: 14px; letter-spacing: 0.4px; margin-top: 4px; }

  .divider { position: absolute; left: 297px; top: 164px; width: 2px; height: 61px; background: var(--ink); }

  .contacts { position: absolute; left: 320px; top: 160px; list-style: none; }
  .contacts li { display: flex; align-items: center; font-size: 15px; letter-spacing: 1px; height: 22px; margin-bottom: 1px; }
  .contacts svg { width: 11px; height: 11px; margin-right: 5px; fill: var(--accent); }

  .address { position: absolute; left: 0; right: 0; top: 274px; text-align: center; font-size: 14px; letter-spacing: 0.2px; }
  .products { position: absolute; left: 0; right: 0; top: 326px; text-align: center; font-weight: 600; font-size: 15px; color: var(--ink); letter-spacing: 0.3px; }
</style>
</head>
<body>
  <section class="card card--front">
    <div class="brand brand--comms">
      <svg class="brand__mark" viewBox="0 0 118 118"><circle cx="59" cy="59" r="52" fill="none" stroke="var(--comms)" stroke-width="10"/></svg>
      <div class="brand__name">VARNEK</div>
      <div class="brand__descriptor">Business Communications</div>
    </div>
    <div class="brand brand--energy">
      <svg class="brand__mark" viewBox="0 0 118 118"><circle cx="59" cy="59" r="52" fill="none" stroke="var(--energy)" stroke-width="10"/></svg>
      <div class="brand__name">VARNEK</div>
      <div class="brand__descriptor">Business Energy</div>
    </div>
  </section>

  <section class="card card--back">
    <div class="back-panel"></div>
    <div class="person">
      <div class="person__name">Lukas Brenner</div>
      <div class="person__role">Geschäftsführer</div>
    </div>
    <div class="divider"></div>
    <ul class="contacts">
      <li><svg viewBox="0 0 24 24"><path d="M6.6 10.8a15.1 15.1 0 0 0 6.6 6.6l2.2-2.2c.3-.3.7-.4 1-.2 1.1.4 2.3.6 3.6.6.6 0 1 .4 1 1V20c0 .6-.4 1-1 1A17 17 0 0 1 3 4c0-.6.4-1 1-1h3.5c.6 0 1 .4 1 1 0 1.3.2 2.5.6 3.6.1.3 0 .7-.2 1z"/></svg>+44 0161 496 0732</li>
      <li><svg viewBox="0 0 24 24"><path d="M2 5h20v14H2z M2 5l10 8 10-8" fill="var(--accent)"/><path d="M2 6l10 8 10-8" fill="none" stroke="#fff" stroke-width="1.5"/></svg>info@varnek-example.co.uk</li>
      <li><svg viewBox="0 0 24 24"><circle cx="12" cy="12" r="10"/><path d="M2 12h20M12 2v20M5 6h14M5 18h14" stroke="#fff" stroke-width="1.3" fill="none"/></svg>varnek-example.co.uk</li>
    </ul>
    <p class="address">24 Alder Row, Manchester, England, M2 7QX</p>
    <p class="products">Business Mobile • Telephony • Internet • Business Energy Solutions</p>
  </section>
</body>
</html>
```